依頼概要
◆本のタイトル
港町グラス日記~灯りの奥のササヤキ~

◆著者
桑原 美津江

◆依頼目的/概要
電子書籍を出版しますので、表紙デザイン作成をお願いいたします。

◆デザイン要望
基本的にお任せです。
イラストや写真等素材を使用される場合には、
商用利用可の素材をお願いします。

色合い、デザイン、レイアウトともデザイナーさんにお任せしたいと思います。

※参考として書籍の原稿を添付します。

◆本の内容
ショットバー”ブルクハルモン”のオーナーバーテンダーである私、桑原美津江が実話をもとに店で繰り広げられる様々な人間ドラマを本にしました。
登場人物であるお客様をヒーロー、ヒロインにするつもりで構成しました。
読者が元気や活力を得て、人生を前向きに生きる一助になることを願い、書き進めました。バーという非日常の空間の中で、臨場感や私とお客様とのやりとりがダイレクトに伝わり、読者の様々な感情を揺さぶることができれば、嬉しく思います。

◆読者ターゲット層
〇30代、40代、50代前半までの働く男性、女性
〇自分の生き方や仕事に漠然とした不安や悩みがある人
〇人生を前向きに自分らしく生きたい人
〇職場間、夫婦間、親子間など人間関係にストレスや問題を抱えている人

◆デザイン要望
〇私が女性バーテンダーで、女性のご来店も多いので、女性が一人でも行ってみたいと思わせる雰囲気のデザイン希望です

〇バーというと敷居が高く、入りにくいイメージを持っている人が多いので、品位は保ちつつもあたたかい雰囲気が伝わるようにしていただきたいです

◆写真素材購入の際は別途写真代をお支払いします。その場合は電子書籍ですので、小サイズで結構です。

◆選定確約です。

◆選定デザインの他に、次点、次々点の方にも報酬をご用意しています。

◆その他、デザインに必要な情報がありましたら、お答えします。
遠慮なく聞いてください。
お盆中で、デザイナーさんから締め切り延長のご希望がありましたので、
2日間だけ、延長することになりました。よろしくお願いします。
■ 選んだ理由

赤、黒、白のデザインは、店と私の雰囲気にぴったりで、とても気に入りました。
オビも読者目線で考えていただき、感謝しています。
おしゃれで元気にもになるそんなデザインに感じました。

■ 提案者全員のお礼・コメント

原稿を読んでくださり、それぞれの強い思いでデザインを考えてくださったのが、
伝わってきました。
お一人、お一人に感謝申し上げます。
良いデザインばかりで、選ぶのに正直とても迷いました。
出版の機会がありましたら、またコンペにご参加くださるとありがたいです。
本当にありがとうございました。

```html
<!DOCTYPE html>
<html lang="ja">
<head>
<meta charset="utf-8">
<title>港町グラス日記 表紙</title>
<link href="https://fonts.googleapis.com/css2?family=Noto+Sans+JP:wght@300;400&family=Oswald:wght@300;400&display=swap" rel="stylesheet">
<style>
  :root {
    --paper: #ffffff;
    --wine-top: #8c1020;
    --wine-mid: #760c1a;
    --wine-bottom: #5c0913;
    --gold: #e9b14c;
    --gold-soft: rgba(233, 177, 76, 0.35);
    --white-soft: rgba(255, 255, 255, 0.22);
    --ink-light: #ffffff;
    --ink-soft: #f1dcdc;
  }
  * { margin: 0; padding: 0; box-sizing: border-box; }
  html, body {
    width: 794px;
    height: 1200px;
    overflow: hidden;
    background: var(--paper);
  }
  .canvas {
    position: relative;
    width: 794px;
    height: 1200px;
    background: var(--paper);
  }
  .cover {
    position: absolute;
    left: 80px;
    top: 92px;
    width: 634px;
    height: 1018px;
    background: linear-gradient(180deg, var(--wine-top) 0%, var(--wine-mid) 55%, var(--wine-bottom) 100%);
    text-align: center;
    color: var(--ink-light);
  }
  .emblem-area {
    position: absolute;
    left: 50%;
    top: 152px;
    width: 112px;
    height: 128px;
    transform: translateX(-50%);
    border-radius: 6px;
    background: linear-gradient(135deg, var(--white-soft) 0%, var(--gold-soft) 100%);
  }
  .title {
    position: absolute;
    left: 0;
    right: 0;
    top: 380px;
    font-family: "Noto Sans JP", sans-serif;
    font-weight: 400;
    font-size: 44px;
    letter-spacing: 0.22em;
    padding-left: 0.22em;
  }
  .title-en {
    position: absolute;
    left: 0;
    right: 0;
    top: 440px;
    font-family: "Oswald", sans-serif;
    font-weight: 300;
    font-size: 22px;
    letter-spacing: 0.28em;
    padding-left: 0.28em;
    color: var(--gold);
  }
  .subtitle {
    position: absolute;
    left: 0;
    right: 0;
    top: 497px;
    font-family: "Noto Sans JP", sans-serif;
    font-weight: 300;
    font-size: 19px;
    letter-spacing: 0.12em;
    color: var(--ink-soft);
  }
  .author {
    position: absolute;
    left: 0;
    right: 0;
    top: 752px;
    font-family: "Noto Sans JP", sans-serif;
    font-weight: 400;
    font-size: 25px;
    letter-spacing: 0.2em;
    padding-left: 0.2em;
  }
  .author-en {
    position: absolute;
    left: 0;
    right: 0;
    top: 798px;
    font-family: "Oswald", sans-serif;
    font-weight: 300;
    font-size: 11px;
    letter-spacing: 0.3em;
    padding-left: 0.3em;
    color: var(--ink-soft);
  }
</style>
</head>
<body>
<div class="canvas">
  <section class="cover">
    <div class="emblem-area" role="img" aria-label="線画のカクテルグラス二つと柑橘の飾り"></div>

    <h1 class="title">港町グラス日記</h1>
    <p class="title-en">HARBOR GLASS DIARY</p>
    <p class="subtitle">〜灯りの奥のササヤキ〜</p>

    <p class="author">桑原 美津江</p>
    <p class="author-en">MITSUE KUWABARA</p>
  </section>
</div>
</body>
</html>
```